Pemberton Dialworks Business Card Design

Double Sided Business Card Design for a Locksmith company specializing in Safecracking, safe & vault service.

```html
<!DOCTYPE html>
<html lang="en">
<head>
<meta charset="utf-8">
<title>Pemberton Dialworks Business Card</title>
<link rel="stylesheet" href="https://fonts.googleapis.com/css2?family=Source+Sans+3:wght@400;600;700;900&display=swap">
<style>
:root{
  --bg:#e3e3e3;
  --ink:#070809;
  --green:#1f7a3b;
  --green-dark:#0c1810;
  --shade:#141617;
  --shade-light:#2a2c2d;
  --white:#ffffff;
  --paper:#f4f4f4;
  --text-dark:#1b1b1b;
  --icon:#2d8a47;
}
*{margin:0;padding:0;box-sizing:border-box}
html,body{width:1200px;height:960px;overflow:hidden}
body{background:var(--bg);font-family:"Source Sans 3",sans-serif;position:relative}
.card{position:absolute;left:305px;width:597px;height:342px;overflow:hidden}
.card-front{top:119px;background:var(--ink)}
.card-back{top:513px;background:var(--paper)}

.front-decor{position:absolute;left:260px;top:-2px;width:620px;height:620px;border-radius:50%;background:var(--green-dark)}
.front-backdrop{position:absolute;left:290px;top:26px;width:307px;height:316px;
  background:radial-gradient(circle at 62% 80%, var(--shade-light) 0, var(--shade) 32%, rgba(20,22,23,.85) 60%, rgba(12,24,16,0) 100%)}
.brand{position:absolute;display:flex;align-items:center;gap:14px}
.brand-mark{border-radius:50%;background:var(--green);flex:none}
.brand-name{font-weight:900;text-transform:uppercase;line-height:.95;letter-spacing:.5px}
.front-brand{left:35px;top:199px}
.front-brand .brand-mark{width:92px;height:92px}
.front-brand .brand-name{color:var(--white);font-size:30px}
.front-web{position:absolute;left:142px;top:286px;color:var(--white);font-size:15px}
.front-web b{color:var(--green);font-weight:700}

.back-top{position:absolute;left:0;top:0;width:100%;height:145px;background:var(--paper)}
.back-brand{left:42px;top:35px}
.back-brand .brand-mark{width:66px;height:66px}
.back-brand .brand-name{color:var(--text-dark);font-size:25px}
.person{position:absolute;right:46px;top:56px;text-align:right}
.person-name{color:var(--green);font-weight:700;font-size:19px;line-height:1.2}
.person-title{color:var(--text-dark);font-size:14.5px;margin-top:2px}

.back-band{position:absolute;left:0;top:145px;width:100%;height:150px;background:var(--ink);overflow:hidden}
.band-decor{position:absolute;left:377px;top:2px;width:186px;height:186px;border-radius:50%;background:var(--green)}
.contact{position:absolute;left:43px;top:12px;color:var(--white);font-size:14.5px;line-height:20px}
.contact .company{color:var(--green)}
.contact ul{list-style:none;margin-top:7px}
.contact li{display:flex;align-items:center;gap:6px}
.contact svg{width:13px;height:13px;fill:var(--icon);flex:none}
.contact b{font-weight:700}

.license{position:absolute;left:40px;top:306px;color:var(--text-dark);font-size:14.5px}
</style>
</head>
<body>

<section class="card card-front">
  <div class="front-decor"></div>
  <div class="front-backdrop" role="img" aria-label="City skyline silhouette with a large safe combination dial"></div>
  <div class="brand front-brand">
    <span class="brand-mark"></span>
    <span class="brand-name">Pemberton<br>Dialworks</span>
  </div>
  <p class="front-web">www.<b>pembertondialworks</b>.com</p>
</section>

<section class="card card-back">
  <div class="back-top">
    <div class="brand back-brand">
      <span class="brand-mark"></span>
      <span class="brand-name">Pemberton<br>Dialworks</span>
    </div>
    <div class="person">
      <p class="person-name">Graham Whitlock</p>
      <p class="person-title">President</p>
    </div>
  </div>

  <div class="back-band">
    <div class="band-decor" role="img" aria-label="Skyline and safe dial in a green circle"></div>
    <div class="contact">
      <p class="company">Pemberton Dialworks LLC</p>
      <p>1840 Harwell Ave, Suite 210</p>
      <p>Dallas , TX , 75204</p>
      <ul>
        <li><svg viewBox="0 0 24 24"><path d="M6.6 10.8a15.5 15.5 0 0 0 6.6 6.6l2.2-2.2c.3-.3.7-.4 1-.2 1.1.4 2.3.6 3.6.6.6 0 1 .4 1 1V20c0 .6-.4 1-1 1A17 17 0 0 1 3 4c0-.6.4-1 1-1h3.5c.6 0 1 .4 1 1 0 1.3.2 2.5.6 3.6.1.3 0 .7-.2 1z"/></svg><span>972-555-0147</span></li>
        <li><svg viewBox="0 0 24 24"><path d="M2 5h20v14H2zm2 2v.5l8 5 8-5V7zm0 2.8V17h16V9.8l-8 5z"/></svg><span>graham@pembertondialworks.com</span></li>
        <li><svg viewBox="0 0 24 24"><path d="M12 2a10 10 0 1 0 0 20 10 10 0 0 0 0-20zm6.9 6h-3a15 15 0 0 0-1.3-3.9A8 8 0 0 1 18.9 8zM12 4c.9 1.2 1.6 2.5 2 4h-4c.4-1.5 1.1-2.8 2-4zM4.3 14a8 8 0 0 1 0-4h3.4a16 16 0 0 0 0 4zm.8 2h3c.3 1.4.8 2.7 1.3 3.9A8 8 0 0 1 5.1 16zm3-8h-3a8 8 0 0 1 4.3-3.9C8.9 5.3 8.4 6.6 8.1 8zM12 20c-.9-1.2-1.6-2.5-2-4h4c-.4 1.5-1.1 2.8-2 4zm2.3-6H9.7a14 14 0 0 1 0-4h4.6a14 14 0 0 1 0 4zm.3 5.9c.5-1.2 1-2.5 1.3-3.9h3a8 8 0 0 1-4.3 3.9zm1.7-5.9a16 16 0 0 0 0-4h3.4a8 8 0 0 1 0 4z"/></svg><span>www.<b>pembertondialworks</b>.com</span></li>
      </ul>
    </div>
  </div>

  <p class="license">Texas DPS Locksmith License# B20481736</p>
</section>

</body>
</html>
```